Text only wordpress site to capture emails

Refer to inspiration upload for list of sites that will be useful for you.

We need a site that will be used to capture emails from clients that follow us on social media. The site will be all text, pretty simple. I have a couple of text sites that I like and we can use them for an example.

Menu section will have home, archive, about.
Footer will have © and Website Privacy Policy | Legal and Policies
There will be some text on the home page and an email capture.

This site will be all text no pictures.

I discuss office politics so the text portions will have some questions and answers on this and then prompt for the visitor to subscribe to my email list.

The only purpose of the site is to build an email list from existing social media followers so the site will be pretty simple in and of itself.

• Text only, similar Q&A to uploaded pics.

I will use a template from letter pinecone dotcom for email capture.

I like the simple couriernew font family that is on both sites supplied in the uploads.
• If you use any color it needs to be very minimal.

```html
<!DOCTYPE html>
<html lang="en">
<head>
<meta charset="utf-8">
<title>Halden Works</title>
<link rel="stylesheet" href="https://fonts.googleapis.com/css2?family=Rokkitt:wght@800&family=Cutive&family=Open+Sans:wght@400;700&display=swap">
<style>
  :root {
    --ink: #222222;
    --muted: #555555;
    --accent: #3b82f6;
    --field: #f3f3f3;
    --field-border: #c9c9c9;
    --button: #9e9e9e;
    --footer: #202020;
    --paper: #ffffff;
    --haze: #ececec;
    --art-light: #eaf1fc;
    --art-mid: #c4d6f3;
  }
  * { margin: 0; padding: 0; box-sizing: border-box; }
  html, body { width: 1200px; height: 686px; overflow: hidden; }
  body {
    position: relative;
    background:
      linear-gradient(to bottom, var(--haze) 0, var(--paper) 170px, var(--paper) 500px, var(--haze) 625px);
    color: var(--ink);
    font-family: "Cutive", serif;
  }
  .site-header {
    position: absolute; top: 30px; left: 110px; right: 112px;
    display: flex; justify-content: space-between; align-items: center;
  }
  .brand {
    font-family: "Rokkitt", serif; font-weight: 800;
    font-size: 22px; letter-spacing: 1px; color: var(--ink);
  }
  .main-nav { display: flex; gap: 34px; }
  .main-nav a {
    font-family: "Cutive", serif; font-size: 13px; color: var(--ink);
    text-decoration: none; padding-bottom: 2px;
  }
  .main-nav a.is-current { color: var(--accent); border-bottom: 3px solid var(--accent); }
  .hero-title {
    position: absolute; top: 196px; left: 110px; width: 480px;
    font-family: "Rokkitt", serif; font-weight: 800;
    font-size: 23px; line-height: 34px; letter-spacing: 1px; text-transform: uppercase;
  }
  .signup { position: absolute; top: 312px; left: 111px; }
  .signup-email {
    display: block; width: 406px; height: 50px;
    background: var(--field); border: 1px solid var(--field-border);
    padding: 0 17px; font-family: "Open Sans", sans-serif; font-size: 15px; color: var(--ink);
  }
  .signup-email::placeholder { color: #7a7a7a; }
  .signup-button {
    display: block; margin-top: 13px; width: 132px; height: 50px; border: 0;
    background: var(--button); color: var(--paper);
    font-family: "Open Sans", sans-serif; font-weight: 700; font-size: 14px; letter-spacing: .3px;
  }
  .intro {
    position: absolute; top: 440px; left: 111px; width: 545px;
    font-size: 13px; line-height: 22.5px; color: var(--muted);
  }
  .hero-art {
    position: absolute; top: 190px; left: 625px; width: 475px; height: 335px;
  }
  .site-footer {
    position: absolute; left: 0; bottom: 0; width: 1200px; height: 61px;
    background: var(--footer); color: var(--paper);
    display: flex; justify-content: center; align-items: center;
    font-size: 13.5px;
  }
  .site-footer a { color: var(--paper); text-decoration: none; }
  .site-footer .sep { margin: 0 7px; }
</style>
</head>
<body>
  <header class="site-header">
    <div class="brand">HALDEN WORKS</div>
    <nav class="main-nav">
      <a href="#" class="is-current">HOME</a>
      <a href="#">ARCHIVE</a>
      <a href="#">ABOUT</a>
    </nav>
  </header>

  <h1 class="hero-title">Lorem ipsum dolor sit amet,<br>consectetur adipiscing elit,<br>sed do eiusmod tempor</h1>

  <form class="signup">
    <input class="signup-email" type="email" placeholder="Email address">
    <button class="signup-button" type="submit">SUBSCRIBE</button>
  </form>

  <p class="intro">Lorem ipsum dolor sit amet, consectetur adipiscing elit, sed do eiusmod tempor incididunt ut labore et dolore magna aliqua. Ut enim ad minim veniam, quis nostrud exercitation ullamco laboris nisi ut aliquip</p>

  <svg class="hero-art" viewBox="0 0 475 335" role="img" aria-label="Illustration of an open envelope with a paper plane and two people subscribing to a newsletter">
    <defs>
      <radialGradient id="art-glow" cx="50%" cy="55%" r="55%">
        <stop offset="0" stop-color="var(--art-mid)"/>
        <stop offset="1" stop-color="var(--art-light)"/>
      </radialGradient>
    </defs>
    <rect x="35" y="30" width="425" height="290" rx="145" fill="url(#art-glow)"/>
  </svg>

  <footer class="site-footer">
    <span>© Halden Works All Rights Reserved</span>
    <span class="sep">|</span>
    <a href="#">Privacy Policy</a>
    <span class="sep">|</span>
    <a href="#">Legal and Policies</a>
  </footer>
</body>
</html>
```